Healthcare IT company looking for business card design

We develop IT systems for healthcare that significantly reduces cost and improves quality.

We want a business card design that is professional and clean, and using the colors in our logo.

Target Market(s)

Doctors and decision makers in the healthcare industry

Industry/Entity Type

Healthcare

Contact Information for Business Card

It should include
Name and title, address, telephone

Tobias Vrenholt, CEO
+46 712 418257
tobias@kelvaro.se

Font styles to use
Serif

Colors
0355a3
ed282f

Requirements
Must have
• Clean design
• Professional feel
Nice to have
• N/A
Should not have
• N/A

```html
<!DOCTYPE html>
<html lang="en">
<head>
<meta charset="utf-8">
<title>Kelvaro Business Card</title>
<link rel="stylesheet" href="https://fonts.googleapis.com/css2?family=Crimson+Pro:ital,wght@0,400;0,600;1,400&display=swap">
<style>
  :root {
    --brand-blue: #0355a3;
    --back-blue: #1c64ae;
    --brand-red: #ed282f;
    --ink: #1a1a1a;
    --paper: #ffffff;
    --edge: #333333;
  }
  html, body {
    margin: 0;
    padding: 0;
    width: 907px;
    height: 1200px;
    overflow: hidden;
    background: var(--paper);
  }
  .sheet {
    position: relative;
    width: 907px;
    height: 1200px;
    font-family: "Crimson Pro", serif;
  }
  .card {
    position: absolute;
    left: 36px;
    width: 835px;
    height: 540px;
    box-sizing: border-box;
    overflow: hidden;
  }
  .card--front {
    top: 38px;
    background: var(--paper);
    border: 1px solid var(--edge);
  }
  .card--back {
    top: 617px;
    background: var(--back-blue);
  }
  .brand-band {
    position: absolute;
    left: 0;
    bottom: 0;
    width: 497px;
    height: 125px;
    background: var(--brand-red);
    border-top-right-radius: 28px;
  }
  .wordmark {
    font-family: "Crimson Pro", serif;
    font-weight: 600;
    font-size: 74px;
    line-height: 1;
    letter-spacing: 0.5px;
    margin: 0;
    display: flex;
    align-items: center;
    gap: 10px;
  }
  .wordmark__dot {
    width: 14px;
    height: 14px;
    background: var(--brand-red);
    display: inline-block;
  }
  .card--front .wordmark {
    position: absolute;
    left: 523px;
    top: 44px;
    color: var(--brand-blue);
  }
  .address {
    position: absolute;
    left: 524px;
    top: 128px;
    margin: 0;
    font-style: italic;
    font-size: 24px;
    color: var(--ink);
  }
  .contact {
    position: absolute;
    left: 524px;
    top: 410px;
    margin: 0;
    font-size: 23px;
    line-height: 29px;
    color: var(--ink);
  }
  .contact p { margin: 0; }
  .card--back .wordmark {
    position: absolute;
    left: 0;
    right: 0;
    top: 225px;
    justify-content: center;
    color: var(--paper);
  }
</style>
</head>
<body>
  <main class="sheet">
    <section class="card card--front" aria-label="Card front">
      <div class="brand-band"></div>
      <h1 class="wordmark">Kelvaro<span class="wordmark__dot"></span></h1>
      <p class="address">Address Line here</p>
      <div class="contact">
        <p class="contact__name">Tobias Vrenholt, CEO</p>
        <p class="contact__phone">Phone: +46 712 418257</p>
        <p class="contact__email">Email: tobias@kelvaro.se</p>
      </div>
    </section>
    <section class="card card--back" aria-label="Card back">
      <h2 class="wordmark">Kelvaro<span class="wordmark__dot"></span></h2>
    </section>
  </main>
</body>
</html>
```